Upscale business cards needed for Board of Directors

We need professional business cards created for members of our family business Board of Directors. We would like these relatively simple and straightforward, but also with a unique element to set them apart. Probably stick with neutral and simple colors - white, grey etc. We need space for the traditional elements, including name, title, address, email/phone number. And we will be creating several from this template so it needs to be template that is easy to switch information in and out of.
Business
See description

```html
<!DOCTYPE html>
<html lang="en">
<head>
<meta charset="utf-8">
<title>Harbourline Holdings – Business Card</title>
<link href="https://fonts.googleapis.com/css2?family=Open+Sans:wght@400;600;700&display=swap" rel="stylesheet">
<style>
  :root {
    --backdrop: #eeeeee;
    --paper: #ffffff;
    --ink: #1f1d1d;
    --ink-soft: #3a3838;
    --charcoal: #2b2727;
    --gold: #b49a68;
    --shadow: rgba(0, 0, 0, 0.12);
  }
  * { box-sizing: border-box; margin: 0; padding: 0; }
  html, body {
    width: 1200px;
    height: 900px;
    overflow: hidden;
    background: var(--backdrop);
    font-family: "Open Sans", Arial, sans-serif;
  }
  .stage {
    width: 1200px;
    height: 900px;
    display: flex;
    flex-direction: column;
    align-items: center;
    justify-content: center;
    gap: 60px;
  }
  .card {
    width: 560px;
    height: 320px;
    position: relative;
    box-shadow: 0 10px 28px var(--shadow);
  }
  .card--front { background: var(--paper); }
  .card--back {
    background: var(--charcoal);
    display: flex;
    align-items: center;
    justify-content: center;
  }
  .person {
    position: absolute;
    left: 36px;
    top: 34px;
  }
  .person__name {
    color: var(--gold);
    font-weight: 600;
    font-size: 17px;
    letter-spacing: 0.2px;
  }
  .person__title {
    color: var(--ink-soft);
    font-size: 10.5px;
    margin-top: 2px;
  }
  .contact {
    position: absolute;
    left: 36px;
    top: 150px;
    color: var(--ink-soft);
    font-size: 11px;
    line-height: 1.55;
    list-style: none;
  }
  .contact__address { margin-bottom: 4px; }
  .contact__item {
    display: flex;
    align-items: center;
    gap: 7px;
  }
  .contact__icon { width: 10px; height: 10px; flex: none; }
  .contact__item--plain { padding-left: 17px; }
  .wordmark {
    text-align: center;
    font-weight: 700;
    text-transform: uppercase;
    line-height: 1;
  }
  .wordmark__name { font-size: 30px; letter-spacing: 1px; }
  .wordmark__sub { font-size: 14px; letter-spacing: 9px; margin-top: 6px; padding-left: 9px; }
  .card--front .wordmark {
    position: absolute;
    right: 36px;
    top: 128px;
    color: var(--ink);
  }
  .card--back .wordmark { color: var(--gold); }
  .card--back .wordmark__name { font-size: 40px; }
  .card--back .wordmark__sub { font-size: 18px; letter-spacing: 12px; padding-left: 12px; }
</style>
</head>
<body>
<main class="stage">
  <section class="card card--front" aria-label="Card front">
    <div class="person">
      <p class="person__name">Daniel Hartley</p>
      <p class="person__title">Managing Director</p>
    </div>
    <ul class="contact">
      <li class="contact__address">27 Quayside Row, Suite 4<br>Bayview Coast, 204518.</li>
      <li class="contact__item">
        <svg class="contact__icon" viewBox="0 0 10 10" aria-hidden="true"><path d="M2 1 L4 1 L4.6 3 L3.4 4 Q4.5 6 6 6.6 L7 5.4 L9 6 L9 8 Q8.5 9 7.5 9 Q1 8 1 2.5 Q1 1.5 2 1 Z" fill="var(--gold)"/></svg>
        020-555 0147
      </li>
      <li class="contact__item">
        <svg class="contact__icon" viewBox="0 0 10 10" aria-hidden="true"><rect x="0.5" y="2" width="9" height="6.5" rx="0.8" fill="var(--gold)"/><path d="M0.8 2.5 L5 5.6 L9.2 2.5" stroke="#fff" stroke-width="0.9" fill="none"/></svg>
        info@harbourline.example
      </li>
      <li class="contact__item contact__item--plain">www.harbourline.example</li>
    </ul>
    <div class="wordmark">
      <p class="wordmark__name">Harbourline</p>
      <p class="wordmark__sub">Holdings</p>
    </div>
  </section>

  <section class="card card--back" aria-label="Card back">
    <div class="wordmark">
      <p class="wordmark__name">Harbourline</p>
      <p class="wordmark__sub">Holdings</p>
    </div>
  </section>
</main>
</body>
</html>
```